Exciting new aperitif brand needs a great label

Vel-Orin is a wonderful rich new premium-priced bitter aperitif, with a deep red colour, from a 100+ year old distillery (1890) near Turin in the Piedmont region of Italy. Inspired by Torvesi, it is perfectly formulated to elevate the classic Baldetti cocktail (and variations on it). It also goes perfectly in a Spritz or a long mixed drink with soda or tonic. The name Vel-Orin is derived from the French for 'peak' and the Italian word for 'love'.

The label, which should take inspiration from Torvesi, but be distinctively different, can incoporate any number of premium label embellishments (foil, embossing, textures etc) and should be no greater than 11cm (height) x 9cm (width) with any core imagery restricted to a width of c.7cm.

The attached mood board should act as inspiration and colour should largely be restricted to reds, blues, whites and perhaps orange. For completeness, the label should note that the ABV is 25% and the bottle size 70cl.

Target Market(s)

21-45yr olds - equal split female/male

Colors
0054AA
0677BA
7BADD7
CADEEF
E8F1F8
0094D4
00A9DD
6FCCEA
C7EBF8
E9F6FB
EE7325
F08F49
F5BC92
FAE3D3
FDF4ED
EB3D1F
EC4F4E
F09395
F8D3D4
FCEDEE

Requirements
Must have
• Great lettering design on the name Vel-Orin

```html
<!DOCTYPE html>
<html lang="en">
<head>
<meta charset="utf-8">
<title>Vel-Orin Label</title>
<link href="https://fonts.googleapis.com/css2?family=Alike&family=Tinos&display=swap" rel="stylesheet">
<style>
  :root {
    --backdrop: #2a0f15;
    --label-black: #262223;
    --gold: #c9a24a;
    --gold-light: #e2c27a;
    --band-red: #c8322d;
    --cream: #f1e4cf;
    --muted: #cfc7bd;
  }
  html, body {
    margin: 0;
    padding: 0;
    width: 1200px;
    height: 771px;
    overflow: hidden;
    background: var(--backdrop);
  }
  .canvas {
    position: relative;
    width: 1200px;
    height: 771px;
  }
  .label {
    position: absolute;
    left: 324px;
    top: 135px;
    width: 552px;
    height: 500px;
    background: var(--label-black);
    overflow: hidden;
  }
  .rule {
    position: absolute;
    left: 0;
    width: 100%;
    height: 3px;
    background: var(--gold);
  }
  .rule--top { top: 6px; }
  .rule--bottom { top: 491px; }
  .heritage {
    position: absolute;
    top: 84px;
    font-family: "Tinos", serif;
    font-size: 19px;
    color: var(--muted);
    letter-spacing: 0.5px;
  }
  .heritage--since { left: 48px; }
  .heritage--year { right: 44px; }
  .crest {
    position: absolute;
    left: 226px;
    top: 46px;
    width: 100px;
    height: 74px;
  }
  .name-band {
    position: absolute;
    left: 0;
    top: 152px;
    width: 100%;
    height: 150px;
    background: var(--band-red);
    border-top: 3px solid var(--gold);
    border-bottom: 3px solid var(--gold);
    box-sizing: border-box;
    display: flex;
    align-items: center;
    justify-content: center;
  }
  .brand-name {
    font-family: "Alike", serif;
    font-size: 128px;
    line-height: 1;
    color: var(--cream);
    margin: 0;
    letter-spacing: -1px;
    white-space: nowrap;
  }
  .tagline {
    position: absolute;
    top: 338px;
    width: 100%;
    text-align: center;
    font-family: "Tinos", serif;
    font-size: 30px;
    color: var(--gold);
  }
  .specs {
    position: absolute;
    top: 424px;
    width: 100%;
    text-align: center;
    font-family: "Tinos", serif;
    font-size: 20px;
    line-height: 27px;
    color: var(--muted);
  }
</style>
</head>
<body>
<div class="canvas">
  <section class="label">
    <div class="rule rule--top"></div>
    <span class="heritage heritage--since">SINCE</span>
    <svg class="crest" role="img" aria-label="Gold crown crest with laurel leaves" viewBox="0 0 100 74">
      <rect x="0" y="0" width="100" height="74" rx="6" fill="var(--gold)"/>
    </svg>
    <span class="heritage heritage--year">1890</span>
    <div class="name-band">
      <h1 class="brand-name">Vel-Orin</h1>
    </div>
    <p class="tagline">PREMIUM QUALITY</p>
    <div class="specs">ABV 25%<br>70cL</div>
    <div class="rule rule--bottom"></div>
  </section>
</div>
</body>
</html>
```